Business Card Design

I need a business card design for a new company based in Australind, Western Australia. The business is for puppet shows at children's parties, fetes, custom puppet builds, etc.Attached is a picture of Ray Caldwick in silhouette. I was thinking a design of a puppeteer at the top of some stairs talking to a puppet in silhouette but open to suggestions. (Under the willow is named as I do all my puppet builds in the top room of my house (at the Under the willow).

Industry/Entity Type

Business

Contact Information for Business Card

Under The Willow Puppets, Dale Munroe, Puppeteer / Puppet Builder, phone - 0438215076, Puppet shows / Custom Puppet Builds, Working With Children

Requirements
Must have
• Name and Logo on one side. Second side to have business card details.

```html
<!DOCTYPE html>
<html lang="en">
<head>
<meta charset="utf-8">
<title>Under The Willow Puppets – Business Card</title>
<link rel="stylesheet" href="https://fonts.googleapis.com/css2?family=Source+Sans+3:wght@400;600&display=swap">
<style>
  :root {
    --backdrop: #e8e6e3;
    --plum: #650030;
    --paper: #ffffff;
    --ink: #3a3a3a;
    --ink-soft: #555555;
  }
  * { margin: 0; padding: 0; box-sizing: border-box; }
  html, body {
    width: 1200px;
    height: 997px;
    overflow: hidden;
    background: var(--backdrop);
    font-family: "Source Sans 3", sans-serif;
  }
  .canvas {
    width: 1200px;
    height: 997px;
    display: flex;
    align-items: center;
    justify-content: center;
    gap: 48px;
  }
  .card {
    width: 540px;
    height: 310px;
    position: relative;
    box-shadow: 0 2px 6px rgba(0,0,0,0.12);
  }
  .card--front {
    background: var(--plum);
    display: flex;
    align-items: center;
    justify-content: center;
  }
  .card--back { background: var(--paper); }

  .brand-name {
    font-weight: 600;
    line-height: 1.02;
    text-align: left;
  }
  .card--front .brand-name {
    color: var(--paper);
    font-size: 40px;
  }
  .card--back .brand-name {
    position: absolute;
    top: 26px;
    right: 34px;
    color: var(--plum);
    font-size: 30px;
  }

  .contact {
    position: absolute;
    left: 40px;
    bottom: 36px;
    color: var(--ink-soft);
    font-size: 13px;
    line-height: 1.35;
  }
  .contact__name {
    color: var(--plum);
    font-weight: 600;
    font-size: 19px;
    line-height: 1.1;
  }
  .contact__role {
    color: var(--ink);
    font-size: 13.5px;
    margin-bottom: 8px;
  }
  .contact__line {
    display: flex;
    align-items: center;
    gap: 7px;
  }
  .contact__icon { width: 11px; height: 11px; fill: var(--plum); flex: none; }
  .services { list-style: none; margin-top: 2px; }
  .services li {
    display: flex;
    align-items: center;
    gap: 8px;
  }
  .services li::before {
    content: "";
    width: 5px;
    height: 5px;
    border-radius: 50%;
    background: var(--plum);
    flex: none;
  }
</style>
</head>
<body>
<main class="canvas">
  <section class="card card--front" aria-label="Card front">
    <p class="brand-name">Under The<br>Willow<br>Puppets</p>
  </section>

  <section class="card card--back" aria-label="Card back">
    <p class="brand-name">Under The<br>Willow<br>Puppets</p>

    <div class="contact">
      <p class="contact__name">Dale Munroe</p>
      <p class="contact__role">Puppeteer / Puppet Builder</p>
      <p class="contact__line">
        <svg class="contact__icon" viewBox="0 0 24 24" aria-hidden="true"><path d="M6.6 10.8a15.2 15.2 0 0 0 6.6 6.6l2.2-2.2a1 1 0 0 1 1-.25 11.4 11.4 0 0 0 3.6.57 1 1 0 0 1 1 1V20a1 1 0 0 1-1 1A17 17 0 0 1 3 4a1 1 0 0 1 1-1h3.5a1 1 0 0 1 1 1c0 1.25.2 2.45.57 3.57a1 1 0 0 1-.25 1z"/></svg>
        0438215076
      </p>
      <p class="contact__line">
        <svg class="contact__icon" viewBox="0 0 24 24" aria-hidden="true"><path d="M2 5h20v14H2z M2 5l10 8 10-8" fill="var(--plum)" stroke="#fff" stroke-width="1.6"/></svg>
        hello@willowpuppets.com
      </p>
      <ul class="services">
        <li>Puppet shows</li>
        <li>Custom Puppet Builds</li>
        <li>Working With Children - 1593862</li>
      </ul>
    </div>
  </section>
</main>
</body>
</html>
```